Wizards Among Humbug Trades*

I am looking for a book cover which will really pop. Working title: Wizards Among Humbug Trades (or W.A.H.T. for short) The concept behind the book is: education is too expensive, screwed up, and basically failing us, and even an MBA is not worth it's name anymore! How a BS is Brilliantly Stupid, a BA is great to be a Broke Artist, an MA is Mostly Antiquated and a MS Mastered Something? ...you get the point, basically I'll be ripping into a whole bunch of degree types, then walking you through what you should actually learn from an MBA. It is going to be written with a fair bit of humor, while still being fact driven. Target audience is working professionals who are considering an MBA, or have one and want a $15 refresher of all they spent $90k+ on. No color scheme is requested, Since i do like to allow creativity to flow!

Book size 5" by 8" and ebook. Author is: L.K. Brannigan size format attached.

Went on vacation/holiday

Colors

Requirements
Must have
• W.A.H.T. (but can be an emphasises in the Wizards Among Humbug Trades title.
Nice to have
• If you look at "A quiet orchard year: notes on tending pears while raising twin goats" on quorvel, you can see a blue/silver/white color scheme I liked in the past - but dont take that as a must by any means, the second choice was a completely different (red and white) scheme

```html
<!DOCTYPE html>
<html lang="en">
<head>
<meta charset="UTF-8">
<title>Wizards Among Humbug Trades — Book Cover</title>
<link rel="stylesheet" href="https://fonts.googleapis.com/css2?family=Archivo:wght@800;900&family=Big+Shoulders+Display:wght@800;900&family=Libre+Baskerville&display=swap">
<style>
  :root {
    --page-bg: #eceff2;
    --cover-bg: #ffffff;
    --navy: #0c3574;
    --steel: #4a74a8;
    --red: #e91c29;
    --ink: #111111;
    --photo-top: #6e7fae;
    --photo-mid: #8a8fa8;
    --photo-low: #a98f86;
    --photo-dark: #1e1f26;
  }
  * { margin: 0; padding: 0; box-sizing: border-box; }
  html, body {
    width: 1200px;
    height: 800px;
    overflow: hidden;
    background: var(--page-bg);
  }
  .book-cover {
    position: absolute;
    left: 350px;
    top: 27px;
    width: 500px;
    height: 746px;
    background: var(--cover-bg);
    overflow: hidden;
    box-shadow: 0 6px 24px rgba(0,0,0,0.18);
  }
  .cover-photo {
    position: absolute;
    left: 0;
    top: 0;
    width: 450px;
    height: 640px;
  }
  .title-lead {
    position: absolute;
    left: 0;
    top: 62px;
    width: 100%;
    text-align: center;
    font-family: "Archivo", sans-serif;
    font-weight: 900;
    font-size: 86px;
    line-height: 1;
    letter-spacing: -1px;
    background: linear-gradient(90deg, var(--navy) 0%, var(--navy) 50%, var(--steel) 62%, var(--steel) 100%);
    -webkit-background-clip: text;
    background-clip: text;
    color: transparent;
  }
  .title-joiner {
    position: absolute;
    left: 47px;
    top: 145px;
    width: 410px;
    display: flex;
    align-items: center;
    gap: 12px;
    font-family: "Archivo", sans-serif;
    font-weight: 800;
    font-size: 30px;
    color: var(--navy);
    line-height: 1;
  }
  .title-joiner .rule {
    flex: 1;
    height: 2px;
    background: var(--navy);
  }
  .title-main {
    position: absolute;
    left: 0;
    width: 100%;
    text-align: center;
    font-family: "Big Shoulders Display", sans-serif;
    font-weight: 900;
    color: var(--red);
    line-height: 1;
    text-shadow: 0 0 3px #fff, 0 0 3px #fff, 0 0 5px #fff, 2px 2px 0 #fff, -2px -2px 0 #fff, 2px -2px 0 #fff, -2px 2px 0 #fff;
  }
  .title-main.first { top: 186px; font-size: 96px; letter-spacing: 2px; }
  .title-main.second { top: 286px; font-size: 150px; letter-spacing: 1px; }
  .short-title {
    position: absolute;
    left: 0;
    top: 452px;
    width: 100%;
    text-align: center;
    font-family: "Archivo", sans-serif;
    font-weight: 800;
    font-size: 32px;
    color: var(--navy);
    text-shadow: 0 0 4px #fff, 0 0 4px #fff;
  }
  .author {
    position: absolute;
    left: 0;
    top: 686px;
    width: 100%;
    text-align: center;
    font-family: "Libre Baskerville", serif;
    font-size: 30px;
    letter-spacing: 3px;
    color: var(--ink);
  }
</style>
</head>
<body>
  <main class="book-cover">
    <svg class="cover-photo" viewBox="0 0 450 640" role="img" aria-label="Photo of a tattooed man in a t-shirt, shorts and high-top sneakers sitting on a black rolling suitcase, shown from the shoulders down">
      <defs>
        <linearGradient id="photoTone" x1="0" y1="0" x2="0.3" y2="1">
          <stop offset="0" stop-color="var(--photo-top)"/>
          <stop offset="0.45" stop-color="var(--photo-mid)"/>
          <stop offset="0.7" stop-color="var(--photo-low)"/>
          <stop offset="1" stop-color="var(--photo-dark)"/>
        </linearGradient>
      </defs>
      <rect x="0" y="0" width="450" height="640" rx="0" fill="url(#photoTone)" opacity="0.55"/>
    </svg>

    <h1 class="title-block">
      <span class="title-lead">WIZARDS</span>
      <span class="title-joiner"><span class="rule"></span>AMONG<span class="rule"></span></span>
      <span class="title-main first">HUMBUG</span>
      <span class="title-main second">TRADES</span>
    </h1>
    <p class="short-title">W.A.H.T.</p>
    <p class="author">L.K. BRANNIGAN</p>
  </main>
</body>
</html>
```